TVQ-Business Card Design

I need a modern, professional business card design that includes my logo as the main feature, maybe the entire background with the contact info overlaying or even contact info on the back and the logo full frontal

Neat and organized placement of contact information

Would like to see options in black and white

Target Market(s)

real estate Developers, Construction managers, business and home owners

Industry/Entity Type

Construction

Contact Information for Business Card

TVQ Construction
Dennis Fairweather
General Contractor

Office: 1-888-902-7351 Ext #1
Cell: 412-730-2168
Fax: 1-888-902-7351

Font styles to use
Serif

Requirements
Must have
• title
• office #
• cell #
• Email
• website
Nice to have
• fax

```html
<!DOCTYPE html>
<html lang="en">
<head>
<meta charset="utf-8">
<title>TVQ Construction – Business Card</title>
<link rel="stylesheet" href="https://fonts.googleapis.com/css2?family=Questrial&display=swap">
<style>
  :root {
    --backdrop: #e4e6e8;
    --card-white: #ffffff;
    --card-black: #000000;
    --forest: #146c3c;
    --lime: #7dc242;
    --text-light: #ffffff;
  }
  html, body {
    margin: 0;
    padding: 0;
    width: 1200px;
    height: 927px;
    overflow: hidden;
    background: var(--backdrop);
    font-family: "Questrial", sans-serif;
  }
  .stage {
    position: relative;
    width: 1200px;
    height: 927px;
  }
  .card {
    position: absolute;
    top: 102px;
    width: 414px;
    height: 723px;
    box-shadow: 8px 10px 18px rgba(0,0,0,0.28);
    overflow: hidden;
  }
  .card--front { left: 164px; background: var(--card-white); }
  .card--back  { left: 623px; background: var(--card-black); }

  .brand {
    position: absolute;
    left: 0;
    width: 100%;
    display: flex;
    align-items: center;
    justify-content: center;
    gap: 12px;
    color: var(--lime);
    font-size: 38px;
    letter-spacing: 1px;
    white-space: nowrap;
  }
  .brand__square {
    width: 26px;
    height: 26px;
    background: var(--lime);
  }
  .card--front .brand { top: 180px; color: var(--forest); }
  .card--front .brand__square { background: var(--forest); }
  .card--back .brand { top: 342px; }

  .divider {
    position: absolute;
    left: 0;
    top: 376px;
    width: 100%;
    height: 2px;
    background: var(--forest);
  }
  .contact-band {
    position: absolute;
    left: 0;
    top: 382px;
    width: 100%;
    height: 341px;
    background: var(--forest);
    text-align: center;
    color: var(--text-light);
  }
  .contact-band__name {
    margin: 73px 0 0;
    font-size: 28px;
    color: var(--lime);
    font-weight: 400;
    letter-spacing: 0.3px;
  }
  .contact-band__title {
    margin: 2px 0 0;
    font-size: 18px;
    letter-spacing: 0.5px;
  }
  .contact-band__icons {
    display: block;
    margin: 30px auto 0;
  }
  .contact-band__list {
    list-style: none;
    margin: 12px 0 0;
    padding: 0;
    font-size: 18px;
    line-height: 22.4px;
    letter-spacing: 0.5px;
  }
  .web-line {
    position: absolute;
    left: 0;
    top: 482px;
    width: 100%;
    text-align: center;
    font-size: 22px;
    color: var(--text-light);
    letter-spacing: 0.5px;
  }
  .web-line__domain { color: var(--lime); }
</style>
</head>
<body>
<div class="stage">

  <section class="card card--front">
    <div class="brand"><span class="brand__square"></span>TVQ Construction</div>
    <div class="divider"></div>
    <div class="contact-band">
      <h1 class="contact-band__name">Dennis Fairweather</h1>
      <p class="contact-band__title">General Contractor</p>
      <svg class="contact-band__icons" width="96" height="16" viewBox="0 0 96 16" fill="none" stroke="#7dc242" stroke-width="1.4">
        <rect x="2" y="1" width="8" height="14" rx="1.5"/>
        <line x1="5" y1="12.5" x2="7" y2="12.5"/>
        <rect x="22" y="6" width="16" height="7" rx="1"/>
        <rect x="25" y="2" width="10" height="4"/>
        <rect x="26" y="11" width="8" height="4" fill="#7dc242"/>
        <path d="M47 2 l3 0 l1.5 4 l-2 1.5 c1 2.5 2.5 4 5 5 l1.5 -2 l4 1.5 l0 3 c-7 0 -13 -6 -13 -13z"/>
        <rect x="66" y="3" width="14" height="10" rx="1"/>
        <polyline points="66,3.5 73,9 80,3.5"/>
        <circle cx="89" cy="8" r="6.5"/>
        <ellipse cx="89" cy="8" rx="2.8" ry="6.5"/>
        <line x1="82.5" y1="8" x2="95.5" y2="8"/>
      </svg>
      <ul class="contact-band__list">
        <li>412-730-2168</li>
        <li>1-888-902-7351</li>
        <li>1-888-902-7351 Ext #1</li>
        <li>info@dennisfairweather.com</li>
        <li>www.tvqconstruction.com</li>
      </ul>
    </div>
  </section>

  <section class="card card--back">
    <div class="brand"><span class="brand__square"></span>TVQ Construction</div>
    <p class="web-line">www.<span class="web-line__domain">tvqconstruction</span>.com</p>
  </section>

</div>
</body>
</html>
```